Non-profit sports organization needs templates for Word and InDesign

"Pelo Minis" is a non-profit organization in Winterthur, which supports the recruitment of young talent by the handball clubs in Winterthur. Every year we run several camps, a tournament for schoolchildren and several handball lessons at school.
During these activities there are always written information. So far we have not given much thought to the design. But since we think that a professional design will also lead to more interaction, we now turn to you as a designer.

For the communication with partners, sponsors, patrons, etc. we need a uniform appearance. Since different departments are currently working with different programs, we need a template for letters and documentation for Word and InDesign.

We will need the documentation template for project descriptions, information, etc.
The letter templates are needed to contact sponsors, authorities, patrons, etc.

Both the letter template and the documentation template should look modern. The design should be based on the existing flyers. Otherwise we have no other requirements so far.

Homepage: www.pelo-minis.ch

Target Market(s)

Letters, documentation or information to authorities, sponsors, associations, patrons, members, participants, etc.

Requirements
Must have
• In addition to the design, the templates should also contain a concept for titles, paragraphs, lists, etc. (colors / fonts / ...)

Word and Indesign templates

```html
<!DOCTYPE html>
<html lang="en">
<head>
<meta charset="utf-8">
<title>Pelo Minis – Letterhead and Cover</title>
<link href="https://fonts.googleapis.com/css2?family=Ubuntu:wght@500;700&family=Tinos&display=swap" rel="stylesheet">
<style>
  :root {
    --backdrop: #d8d8d8;
    --letter-paper: #e9e9e9;
    --cover-paper: #f4f4f4;
    --brand-blue: #0a5cad;
    --brand-red: #d2101a;
    --soft-blue: #8ec8e4;
    --ink: #1c1c1c;
  }
  * { margin: 0; padding: 0; box-sizing: border-box; }
  html, body { width: 1200px; height: 823px; overflow: hidden; }
  body { background: var(--backdrop); position: relative; }

  .sheet { position: absolute; }
  .letterhead { left: 119px; top: 100px; width: 445px; height: 628px; background: var(--letter-paper); }
  .cover { left: 601px; top: 95px; width: 450px; height: 637px; background: var(--cover-paper); }

  .brand-name {
    position: absolute;
    font-family: "Ubuntu", sans-serif;
    font-weight: 700;
    color: var(--brand-blue);
    white-space: nowrap;
  }
  .letterhead .brand-name { left: 64px; top: 69px; font-size: 21px; }

  .contact {
    position: absolute; left: 325px; top: 62px;
    font-family: "Ubuntu", sans-serif; font-weight: 500;
    font-size: 6.4px; line-height: 8.5px; color: var(--ink);
    white-space: nowrap;
  }
  .contact .contact-name { font-weight: 700; font-size: 8.6px; line-height: 9px; color: var(--brand-blue); }
  .contact .contact-gap { height: 8px; }
  .contact .label { display: inline-block; width: 11.5px; }

  .edge-tab { position: absolute; right: 0; top: 47px; width: 17px; height: 58px; background: var(--brand-blue); }

  .letter-body {
    position: absolute; left: 67px; top: 158px; width: 330px;
    font-family: "Tinos", serif; font-size: 9.1px; line-height: 10.1px; color: var(--ink);
    white-space: nowrap;
  }
  .letter-body p { margin-bottom: 10px; }
  .letter-body .gap-20 { margin-bottom: 21px; }
  .letter-body .gap-25 { margin-bottom: 25px; }

  .footer-rule { position: absolute; top: 605px; height: 2px; }
  .footer-rule.red { left: 67px; width: 80px; background: var(--brand-red); }
  .footer-rule.blue { left: 149px; width: 249px; background: var(--brand-blue); }

  .cover .brand-name {
    left: 0; width: 100%; top: 282px; text-align: center;
    font-size: 46px; color: var(--soft-blue);
  }
</style>
</head>
<body>

  <section class="sheet letterhead">
    <div class="brand-name">Pelo Minis</div>

    <div class="contact">
      <div class="contact-name">Pelo Minis</div>
      <div>4710 Brenzach</div>
      <div class="contact-gap"></div>
      <div><span class="label">E</span>info@pelo-minis.ch</div>
      <div><span class="label">W</span>www.pelo-minis.ch</div>
    </div>

    <div class="edge-tab"></div>

    <div class="letter-body">
      <p>Ashford, NY 11408</p>
      <p class="gap-20">June 28, 2007</p>
      <p class="gap-20">Ms. Clara Mendel<br>Riverside Fellowship<br>&nbsp;&nbsp;48 Elm Street<br>Hartwell, NY 10432</p>
      <p>Dear Ms. Mendel:</p>
      <p class="gap-25">The Riverside Fellowship has always loomed on the horizon for me. Ever since I<br>decided to major in history, I have wanted to participate in your program. From the<br>research that I have done, I believe that your program provides its participants with<br>an extensively detailed look at the history of the world through hands-on<br>experience with fossils, artifacts, and other remains that compose the blueprint of<br>our existence. &nbsp;I am applying for the Riverside Fellowship because I believe that it<br>would benefit me throughout my career and allow me to further understand the<br>ideas behind history and how it is constructed.</p>
      <p>I believe my skills, experience, and goals make me an excellent candidate for your<br>program.</p>
      <p class="gap-20">Thank you very much for considering me for the Riverside Fellowship. I am<br>looking forward to hearing from you.</p>
      <p>Sincerely,</p>
      <p>Marlen<br>(555) 214-0937</p>
    </div>

    <div class="footer-rule red"></div>
    <div class="footer-rule blue"></div>
  </section>

  <section class="sheet cover">
    <div class="brand-name">Pelo Minis</div>
  </section>

</body>
</html>
```